- Redesign our business card
- Logo remains unchanged
- Current business card attached

Target Market(s)

We are a property management company

Industry/Entity Type

Business

```html
<!DOCTYPE html>
<html lang="en">
<head>
<meta charset="utf-8">
<title>Harlow Property Group – Business Cards</title>
<link rel="stylesheet" href="https://fonts.googleapis.com/css2?family=Roboto:wght@300;400;700&display=swap">
<style>
  :root {
    --page: #ffffff;
    --ink: #000000;
    --cream: #f3efe1;
    --olive: #7b7b3f;
    --stone: #6b6c6e;
    --sand: #dfd3a8;
    --text-grey: #5a5a5a;
    --rule: #8a8a8a;
  }
  * { box-sizing: border-box; margin: 0; padding: 0; }
  html, body { width: 1200px; height: 813px; overflow: hidden; background: var(--page); }
  body { font-family: "Roboto", Arial, sans-serif; }
  .sheet { position: relative; width: 1200px; height: 813px; }
  .divider { position: absolute; left: 543px; top: 92px; width: 1px; height: 620px; background: var(--rule); }

  .card { position: absolute; width: 476px; height: 265px; overflow: hidden; }
  .card--dark { background: var(--ink); }
  .card--light { background: var(--cream); }
  .card--front-dark { left: 37px; top: 111px; }
  .card--front-light { left: 576px; top: 111px; }
  .card--back-light { left: 35px; top: 446px; }
  .card--back-dark { left: 577px; top: 446px; }

  .brand-mark { position: absolute; left: 50px; top: 56px; width: 120px; height: 120px; background: var(--olive); }

  .services { position: absolute; left: 264px; top: 72px; list-style: none; font-size: 14px; line-height: 26px; }
  .card--dark .services { color: var(--sand); font-weight: 400; }
  .card--light .services { color: var(--stone); font-weight: 700; left: 258px; top: 70px; }

  .brand-name { position: absolute; left: 52px; top: 188px; font-size: 21px; font-weight: 400; letter-spacing: 2.4px; color: var(--stone); }
  .brand-tagline { position: absolute; left: 52px; top: 215px; font-size: 15px; font-weight: 400; letter-spacing: 1.6px; color: var(--stone); }
  .card--dark .brand-tagline { color: #8e8e8e; }

  .contact { position: absolute; left: 32px; top: 27px; font-weight: 300; }
  .contact__name { font-size: 20px; line-height: 24px; }
  .contact__role { font-size: 14px; line-height: 20px; margin-bottom: 18px; }
  .contact__line { font-size: 15px; line-height: 20px; }
  .contact__web { font-size: 15px; line-height: 21px; font-weight: 700; }
  .card--light .contact { color: var(--text-grey); }
  .card--dark .contact { color: var(--sand); }
  .label { display: inline-block; width: 16px; }

  .corner-mark { position: absolute; right: 30px; bottom: 0; width: 100px; height: 100px; background: var(--olive); }
</style>
</head>
<body>
<main class="sheet">
  <div class="divider"></div>

  <section class="card card--dark card--front-dark">
    <div class="brand-mark"></div>
    <ul class="services">
      <li>STRATA MANAGEMENT</li>
      <li>COMMUNITY MANAGEMENT</li>
      <li>PROPERTY MANAGEMENT</li>
    </ul>
    <p class="brand-name">HARLOW PROPERTY GROUP</p>
    <p class="brand-tagline">STRATA MANAGEMENT SERVICES</p>
  </section>

  <section class="card card--light card--front-light">
    <div class="brand-mark"></div>
    <ul class="services">
      <li>STRATA MANAGEMENT</li>
      <li>COMMUNITY MANAGEMENT</li>
      <li>PROPERTY MANAGEMENT</li>
    </ul>
    <p class="brand-name">HARLOW PROPERTY GROUP</p>
    <p class="brand-tagline">STRATA MANAGEMENT SERVICES</p>
  </section>

  <section class="card card--light card--back-light">
    <div class="contact">
      <p class="contact__name">daniel marsh</p>
      <p class="contact__role">licensed strata manager</p>
      <p class="contact__line">po box 48, elmwood nsw 2090</p>
      <p class="contact__line">12/5-19 carrow street redfield nsw 2016</p>
      <p class="contact__line"><span class="label">t:</span> 02 5550 0360</p>
      <p class="contact__line"><span class="label">f:</span> 02 5550 4830</p>
      <p class="contact__line"><span class="label">m:</span> 0400 555 017</p>
      <p class="contact__line"><span class="label">e:</span> info@harlowproperty.example</p>
      <p class="contact__web">www.harlowproperty.example</p>
    </div>
    <div class="corner-mark"></div>
  </section>

  <section class="card card--dark card--back-dark">
    <div class="contact">
      <p class="contact__name">daniel marsh</p>
      <p class="contact__role">licensed strata manager</p>
      <p class="contact__line">po box 48, elmwood nsw 2090</p>
      <p class="contact__line">12/5-19 carrow street redfield nsw 2016</p>
      <p class="contact__line"><span class="label">t:</span> 02 5550 0360</p>
      <p class="contact__line"><span class="label">f:</span> 02 5550 4830</p>
      <p class="contact__line"><span class="label">m:</span> 0400 555 017</p>
      <p class="contact__line"><span class="label">e:</span> info@harlowproperty.example</p>
      <p class="contact__web">www.harlowproperty.example</p>
    </div>
    <div class="corner-mark"></div>
  </section>
</main>
</body>
</html>
```